Chocolate covered bananas

“I am starting a new venture making chocolate coated frozen bananas. At start up I intend to have 4 different types:
3 will be single bananas ( Dark Chocolate, Dark chocolate with sprinkles and Dark Chocolate & Almonds) sold in individual packets, 70MM(W) x 215mm(L)

The other will be Banana Pops (smaller pieces of banana) sold in a 500g bag and then packed in a 165mm(L) x 50mm(W) X 165mm(H) cardboard box

The packaging will need my logo the wording “Chocolate Coated Frozen Banana” and the slogan “Sweet Bite Delight” on it. A picture of a Banana and Chocolate (The chocolate can be on the banana, getting poured on it, or even beside it).
I would like the words “Zero Trans-fat” on both the packaging (3 variations) and the 500g container along with “Healthy Dessert Treat” on the Container.

I need the Ingredients and nutritional information on the back"

one version can be submitted within the Contest period, however the winner is required to provide all 4 versions as part of the project.

Good Luck
Updates

JUST A QUICK NOTE THE BANANAS WILL BE ON A ICE-CREAM STICK AND THE BANANA POPS WILL BE ON A POPSICLE STICK.

Here are a couple of examples from places in America (no competition to me I am in another country) I'm am looking for something similar in size. as the packets in wholly mangoes and the cartons in gretas melons. http://www.wholly-mangoes.net/products.php and http://www.gretasmelons.com/our-products/ I hope this helps Regards Colin.

Hi I am getting some great designs Most are dark brown (or chocolate ) in colour they look good however most ice cream packs are dark and I think in order for these to stand out they need to be brighter with the chocolate as a secondary colour. Regards Colin.

Hi all great designs it will be very hard to pick. just a quick note I made a spelling mistake in my brief it is HEALTHY DESSERT TREAT (NOT DESERT) SORRY Regards Colin.

I would like to thank everyone for there time and effort they have put in to my packaging design contest. I am meeting with the packaging company on Thursday and will have a decision Thursday night. Regards Colin.

Target Market(s)

I plan to go down the track that these are a healthy tasty fun treat.
I will be using real Bananas and Real chocolate.

```html
<!DOCTYPE html>
<html lang="en">
<head>
<meta charset="utf-8">
<title>Golden Dip Co – Chocolate Coated Frozen Banana, Dark Chocolate</title>
<link href="https://fonts.googleapis.com/css2?family=Antonio:wght@400;600&display=swap" rel="stylesheet">
<style>
  :root {
    --backdrop: #fde9d6;
    --wrap-top: #f2b263;
    --wrap-mid: #fdddaa;
    --wrap-low: #f7c98e;
    --choc-dark: #4a2412;
    --choc-mid: #6b3a1e;
    --choc-light: #8a5230;
    --cream: #fbe8c8;
    --title-fill: #f9e27a;
    --title-stroke: #3b1d0c;
    --slice-tone: #f3e6b4;
    --stick-tone: #dcb47c;
  }
  html, body {
    margin: 0;
    padding: 0;
    width: 1200px;
    height: 2880px;
    overflow: hidden;
    background: var(--backdrop);
  }
  .canvas { display: block; width: 1200px; height: 2880px; }
  .wrap-body { fill: url(#wrapGradient); }
  .wrap-sheen { fill: url(#sheenGradient); }
  .choc-band { fill: url(#chocGradient); }
  .crimp-top { fill: url(#crimpTop); }
  .crimp-bottom { fill: url(#crimpBottom); }
  .brand-dot { fill: var(--choc-dark); }
  .brand-name {
    font-family: "Antonio", sans-serif;
    font-weight: 600;
    font-size: 46px;
    fill: var(--choc-dark);
  }
  .product-title {
    font-family: "Antonio", sans-serif;
    font-weight: 400;
    font-size: 100px;
    fill: var(--title-fill);
    stroke: var(--title-stroke);
    stroke-width: 4px;
    paint-order: stroke;
  }
  .treat-placeholder { fill: url(#treatGradient); }
  .slice-placeholder { fill: var(--slice-tone); opacity: 0.9; }
  .badge-shape { fill: var(--cream); }
  .badge-text {
    font-family: "Antonio", sans-serif;
    font-weight: 400;
    font-size: 44px;
    fill: var(--choc-mid);
  }
  .flavour-ribbon { fill: var(--cream); }
  .flavour-name {
    font-family: "Antonio", sans-serif;
    font-weight: 600;
    font-size: 88px;
    fill: var(--choc-dark);
  }
  .net-weight {
    font-family: "Antonio", sans-serif;
    font-weight: 400;
    font-size: 38px;
    fill: var(--cream);
  }
</style>
</head>
<body>
<svg class="canvas" viewBox="0 0 1200 2880" xmlns="http://www.w3.org/2000/svg">
  <defs>
    <linearGradient id="wrapGradient" x1="0" y1="0" x2="0" y2="1">
      <stop offset="0" stop-color="var(--wrap-top)"/>
      <stop offset="0.35" stop-color="var(--wrap-mid)"/>
      <stop offset="0.7" stop-color="var(--wrap-low)"/>
      <stop offset="1" stop-color="var(--wrap-top)"/>
    </linearGradient>
    <linearGradient id="sheenGradient" x1="0" y1="0" x2="1" y2="0">
      <stop offset="0" stop-color="#fff" stop-opacity="0.3"/>
      <stop offset="0.08" stop-color="#fff" stop-opacity="0"/>
      <stop offset="0.9" stop-color="#fff" stop-opacity="0"/>
      <stop offset="0.97" stop-color="#fff" stop-opacity="0.35"/>
      <stop offset="1" stop-color="#fff" stop-opacity="0.1"/>
    </linearGradient>
    <linearGradient id="chocGradient" x1="0" y1="0" x2="0" y2="1">
      <stop offset="0" stop-color="var(--choc-light)"/>
      <stop offset="0.3" stop-color="var(--choc-dark)"/>
      <stop offset="1" stop-color="var(--choc-mid)"/>
    </linearGradient>
    <linearGradient id="treatGradient" x1="0" y1="0" x2="0" y2="1">
      <stop offset="0" stop-color="var(--choc-mid)"/>
      <stop offset="0.78" stop-color="var(--choc-dark)"/>
      <stop offset="0.8" stop-color="var(--stick-tone)"/>
      <stop offset="1" stop-color="var(--stick-tone)"/>
    </linearGradient>
    <clipPath id="wrapClip">
      <rect x="240" y="254" width="720" height="2384"/>
    </clipPath>
    <pattern id="crimpTop" x="240" y="240" width="20" height="14" patternUnits="userSpaceOnUse">
      <path d="M0 14 L10 0 L20 14 Z" fill="var(--wrap-top)"/>
    </pattern>
    <pattern id="crimpBottom" x="240" y="2638" width="20" height="14" patternUnits="userSpaceOnUse">
      <path d="M0 0 L10 14 L20 0 Z" fill="var(--choc-mid)"/>
    </pattern>
  </defs>

  <!-- wrapper -->
  <rect class="crimp-top" x="240" y="240" width="720" height="14"/>
  <rect class="wrap-body" x="240" y="254" width="720" height="2384"/>
  <rect class="choc-band" role="img" aria-label="Splash of melted dark chocolate" x="240" y="2088" width="720" height="550"/>
  <rect class="crimp-bottom" x="240" y="2638" width="720" height="14"/>

  <!-- banana slice placeholders -->
  <g clip-path="url(#wrapClip)">
    <circle class="slice-placeholder" role="img" aria-label="Banana slice" cx="352" cy="468" r="96"/>
    <circle class="slice-placeholder" role="img" aria-label="Banana slice" cx="870" cy="360" r="108"/>
    <circle class="slice-placeholder" role="img" aria-label="Banana slice" cx="796" cy="1128" r="104"/>
    <circle class="slice-placeholder" role="img" aria-label="Banana slice" cx="396" cy="1476" r="136"/>
    <circle class="slice-placeholder" role="img" aria-label="Banana slice" cx="844" cy="1944" r="110"/>
  </g>

  <rect class="wrap-sheen" x="240" y="254" width="720" height="2384"/>

  <!-- brand -->
  <g class="brand">
    <circle class="brand-dot" cx="486" cy="392" r="16"/>
    <text class="brand-name" x="514" y="408">Golden Dip Co</text>
  </g>

  <!-- title -->
  <g class="product-title-block" text-anchor="middle">
    <text class="product-title" x="624" y="678" textLength="370" lengthAdjust="spacingAndGlyphs">CHOCOLATE</text>
    <text class="product-title" x="624" y="768" textLength="250" lengthAdjust="spacingAndGlyphs">COATED</text>
    <text class="product-title" x="624" y="858" textLength="230" lengthAdjust="spacingAndGlyphs">FROZEN</text>
    <text class="product-title" x="624" y="950" textLength="250" lengthAdjust="spacingAndGlyphs">BANANA</text>
  </g>

  <!-- product placeholder -->
  <rect class="treat-placeholder" role="img" aria-label="Chocolate coated banana on a wooden ice-cream stick" x="440" y="1008" width="400" height="1260" rx="60"/>

  <!-- zero trans-fat badge -->
  <g class="badge" text-anchor="middle">
    <circle class="badge-shape" cx="391" cy="1949" r="92"/>
    <text class="badge-text" x="391" y="1936">Zero</text>
    <text class="badge-text" x="391" y="1988" textLength="140" lengthAdjust="spacingAndGlyphs">Trans-fat</text>
  </g>

  <!-- flavour ribbon -->
  <g class="flavour">
    <path class="flavour-ribbon" d="M343 2400 L893 2400 L873 2460 L893 2520 L343 2520 L363 2460 Z"/>
    <text class="flavour-name" x="618" y="2494" text-anchor="middle" textLength="490" lengthAdjust="spacingAndGlyphs">DARK CHOCOLATE</text>
  </g>

  <text class="net-weight" x="600" y="2598" text-anchor="middle">500g</text>
</svg>
</body>
</html>
```